Need small adjustment to BR organics logo. Have a design to go off.
Then i need the label design completed. i have attached the file as a reference.

Logo Text

Blue Ridge Organics

Colors

Designer to choose colors to be used in the design.

Requirements
Must have
• Info in file attched. Plus the small CBD logos
Should not have
• Remove Blue Ridge Kitchen Appliances under sample design

```html
<!DOCTYPE html>
<html lang="en">
<head>
<meta charset="utf-8">
<title>Blue Ridge Organics – Platinum CBD Oil for Pets Label</title>
<link rel="stylesheet" href="https://fonts.googleapis.com/css2?family=Montserrat:wght@400;500;600;700&family=Smokum&family=Oswald:wght@400&display=swap">
<style>
  :root {
    --page: #f2f2f2;
    --label: #242122;
    --label-center: #1b1919;
    --green: #6cc04a;
    --green-soft: #8fd06b;
    --white: #ffffff;
    --text: #e9e9e9;
    --icon: #cfcfcf;
  }
  * { margin: 0; padding: 0; box-sizing: border-box; }
  html, body { width: 1200px; height: 1200px; overflow: hidden; background: var(--page); }
  body { position: relative; font-family: "Montserrat", sans-serif; }
  h1, h2 { font-weight: 400; }

  .label {
    position: absolute; left: 40px; top: 357px; width: 1120px; height: 485px;
    background: var(--label); display: flex; overflow: hidden;
  }
  .panel { position: relative; height: 100%; }
  .panel--side-left { width: 362px; padding: 40px 24px 0 26px; }
  .panel--front { width: 388px; background: var(--label-center); text-align: center; }
  .panel--side-right { width: 370px; padding: 42px 20px 0 26px; }

  .display { font-family: "Smokum", "Oswald", serif; font-weight: 400; white-space: nowrap; }

  .section-tag {
    display: inline-block; background: var(--green); color: var(--white);
    font-size: 28px; line-height: 36px; padding: 0 16px; border-radius: 3px;
  }
  .section-tag--wide { display: block; width: 308px; }
  .copy {
    color: var(--text); font-size: 14px; font-weight: 500; letter-spacing: 1.6px;
    line-height: 19.5px; text-transform: uppercase; margin: 12px 0 10px;
  }

  .badges { position: absolute; left: 18px; right: 14px; top: 383px; display: flex; justify-content: space-between; }
  .badge { width: 78px; text-align: center; }
  .badge svg { width: 50px; height: 50px; display: block; margin: 0 auto 8px; }
  .badge span {
    display: block; color: var(--icon); font-size: 9px; letter-spacing: 1px;
    line-height: 11px; text-transform: uppercase;
  }

  .brand { padding-top: 34px; }
  .brand-mark { width: 30px; height: 30px; border-radius: 50%; background: var(--green); margin: 0 auto 8px; }
  .brand-name {
    color: var(--white); font-weight: 700; font-size: 17px; letter-spacing: 2.5px;
    line-height: 21px; text-transform: uppercase;
  }
  .grade {
    display: inline-block; margin-top: 20px; width: 238px; height: 36px; line-height: 36px;
    background: var(--green); color: var(--white); border-radius: 4px;
    font-weight: 700; font-size: 22px; letter-spacing: 8px; padding-left: 8px;
  }
  .product-type { display: block; color: var(--green-soft); font-size: 44px; line-height: 46px; margin-top: 12px; }
  .product-name { display: block; color: var(--green); font-size: 96px; line-height: 90px; }
  .audience { color: var(--white); font-weight: 600; font-size: 24px; letter-spacing: 9px; line-height: 30px; margin-top: 12px; padding-left: 9px; }
  .volume { color: var(--green); font-weight: 600; font-size: 18px; letter-spacing: 2px; line-height: 22px; margin-top: 20px; }
  .web { color: var(--white); font-weight: 500; font-size: 15px; line-height: 20px; margin-top: 8px; white-space: nowrap; }
  .web em { font-style: normal; color: var(--green); }

  .divider { height: 3px; background: var(--green); margin: 14px 0 14px; }
  .facts { font-size: 14px; font-weight: 500; letter-spacing: 1.4px; line-height: 19.5px; text-transform: uppercase; color: var(--text); }
  .facts b { font-weight: 500; color: var(--green); }
</style>
</head>
<body>
<main class="label">

  <section class="panel panel--side-left">
    <h2 class="section-tag section-tag--wide display">SUGGESTED USE *</h2>
    <p class="copy">Shake well, fill dropper<br>and place under tongue.<br>Store away from heat, light<br>and humidity.</p>
    <h2 class="section-tag section-tag--wide display">WARNING</h2>
    <p class="copy">Consult with your<br>healthcare provider before<br>using<br>if you are nursing, pregnant<br>or taking medication.If<br>adverse reaction occurs,<br>discontinue.</p>

    <div class="badges">
      <div class="badge">
        <svg viewBox="0 0 50 50" fill="none" stroke="var(--icon)" stroke-width="1.6">
          <circle cx="25" cy="25" r="22"/><line x1="9" y1="41" x2="41" y2="9"/>
          <text x="25" y="30" text-anchor="middle" font-family="Montserrat, sans-serif" font-size="14" fill="var(--icon)" stroke="none">GMO</text>
        </svg><span>No GMO</span>
      </div>
      <div class="badge">
        <svg viewBox="0 0 50 50" fill="none" stroke="var(--icon)" stroke-width="1.6">
          <circle cx="25" cy="25" r="22"/>
          <path d="M25 38 C14 30 16 18 25 11 C34 18 36 30 25 38 Z" fill="var(--green)" stroke="none"/>
          <line x1="25" y1="16" x2="25" y2="40" stroke="var(--label)"/>
        </svg><span>Naturally<br>grown</span>
      </div>
      <div class="badge">
        <svg viewBox="0 0 50 50" fill="none" stroke="var(--icon)" stroke-width="1.6">
          <circle cx="25" cy="25" r="22"/>
          <rect x="21" y="11" width="6" height="14" rx="1"/>
          <path d="M30 20 a9 9 0 0 1 -4 16"/>
          <line x1="15" y1="37" x2="35" y2="37"/><line x1="19" y1="33" x2="29" y2="33"/>
        </svg><span>Lab<br>tested</span>
      </div>
      <div class="badge">
        <svg viewBox="0 0 50 50" fill="none" stroke="var(--icon)" stroke-width="1.6">
          <circle cx="25" cy="25" r="22"/><line x1="9" y1="41" x2="41" y2="9"/>
          <text x="25" y="30" text-anchor="middle" font-family="Montserrat, sans-serif" font-size="14" fill="var(--icon)" stroke="none">THC</text>
        </svg><span>No THC</span>
      </div>
    </div>
  </section>

  <section class="panel panel--front">
    <div class="brand">
      <div class="brand-mark"></div>
      <p class="brand-name">Blue Ridge<br>Organics</p>
    </div>
    <div class="grade">PLATINUM</div>
    <h1>
      <span class="product-type display">BROAD SPECTRUM</span>
      <span class="product-name display">CBD OIL</span>
    </h1>
    <p class="audience">FOR PETS</p>
    <p class="volume">30ML / 250 MG</p>
    <p class="web">WWW.BLUERIDGE<em>ORGANICS</em>.COM.AU</p>
  </section>

  <section class="panel panel--side-right">
    <h2 class="section-tag display">INGREDIENTS</h2>
    <p class="copy">Organically grown<br>Microsorbe* optimized broad<br>spectrum CBD hemp oil,<br>Microsorb* melatonin, MCT oil,<br>natural flavours, stevia.</p>
    <div class="divider"></div>
    <p class="facts"><b>Serving size:</b> 1 dropper (1ml)<br><b>CBD per serving:</b> 20mg<br><b>Serving per bottle:</b> 30</p>

    <div class="badges">
      <div class="badge">
        <svg viewBox="0 0 50 50" fill="none" stroke="var(--icon)" stroke-width="1.6">
          <circle cx="25" cy="25" r="22"/><line x1="25" y1="12" x2="25" y2="40"/>
          <path d="M25 20 l-6 -4 M25 20 l6 -4 M25 27 l-6 -4 M25 27 l6 -4 M25 34 l-6 -4 M25 34 l6 -4"/>
          <line x1="10" y1="40" x2="40" y2="10"/>
        </svg><span>Glutten<br>free</span>
      </div>
      <div class="badge">
        <svg viewBox="0 0 50 50" fill="none" stroke="var(--icon)" stroke-width="1.6">
          <circle cx="25" cy="25" r="22"/><path d="M25 11 C19 21 16 25 16 30 a9 9 0 0 0 18 0 C34 25 31 21 25 11 Z"/>
        </svg><span>100%<br>pure</span>
      </div>
      <div class="badge">
        <svg viewBox="0 0 50 50" fill="none" stroke="var(--icon)" stroke-width="1.6">
          <circle cx="25" cy="25" r="22"/><circle cx="25" cy="25" r="13" stroke-dasharray="3 2"/>
          <circle cx="25" cy="25" r="6" fill="var(--green)" stroke="none"/>
        </svg><span>Industrial<br>hemp</span>
      </div>
      <div class="badge">
        <svg viewBox="0 0 50 50" fill="none" stroke="var(--icon)" stroke-width="1.6">
          <circle cx="25" cy="25" r="22"/>
          <path d="M20 18 h10 l-2 -6 h-8 Z"/><rect x="20" y="18" width="10" height="20" rx="2"/>
          <line x1="10" y1="40" x2="40" y2="10"/>
        </svg><span>Pesticide<br>free</span>
      </div>
    </div>
  </section>

</main>
</body>
</html>
```